Family Ranch with a hobby vineyard needs 2 wine labels for our first harvest

Design 2 wine labels (front and back) with the Brindor Ranch logo.
Label 1:
Sauvignon Blanc
Alc. 12.5% by Vol.
Palos Verdes Peninsula - add as the region
Year 2022
Label 2:
Cabernet Sauvignon
Alc. 13.5% by Vol.
Year 2022
For the back label design:
GOVERNMENT WARNING: (1) According to the Surgeon General, women
should not drink alcoholic beverages during pregnancy because of the risk of
birth defects. (2) Consumption of alcoholic beverages impairs your ability to
drive a car or operate machinery, and may cause health problems.
Contains Sulfates.
750ML
I just received the bottles and have attached a picture.
Look and feel
Each slider illustrates characteristics of the customer's brand and the style your logo design should communicate.

```html
<!DOCTYPE html>
<html lang="en">
<head>
<meta charset="utf-8">
<title>Brindor Ranch – Wine Labels</title>
<link rel="stylesheet" href="https://fonts.googleapis.com/css2?family=Cinzel:wght@600&family=Tinos&display=swap">
<style>
  :root {
    --page: #ffffff;
    --ink: #111111;
    --strip: #0d0d0d;
    --gold-light: #f1d27a;
    --gold-mid: #d3a23f;
    --gold-dark: #a8701c;
    --gold-text: #c9a24a;
    --silver-light: #e9e9ec;
    --silver-mid: #c3c3c8;
    --silver-dark: #8e8e94;
    --silver-text: #b8b8bd;
  }
  * { margin: 0; padding: 0; box-sizing: border-box; }
  html, body { width: 796px; height: 1200px; overflow: hidden; background: var(--page); }
  .canvas {
    position: relative; width: 796px; height: 1200px;
    display: flex; justify-content: space-evenly; align-items: center;
  }
  .label { position: relative; width: 360px; height: 640px; }
  .label--gold { --accent: var(--gold-text); }
  .label--silver { --accent: var(--silver-text); }

  .back-strip {
    position: absolute; left: 90px; top: 0; width: 180px; height: 640px;
    background: var(--strip); padding: 8px;
  }
  .back-strip__frame { width: 100%; height: 100%; border: 1.5px solid var(--accent); }
  .stars {
    position: absolute; top: 18px; left: 0; width: 100%;
    display: flex; justify-content: center; gap: 10px;
  }
  .stars svg { width: 17px; height: 17px; fill: var(--accent); }

  .shield { position: absolute; left: 0; top: 49px; width: 360px; height: 372px; }
  .shield svg { width: 100%; height: 100%; display: block; }

  .front-text {
    position: absolute; left: 0; top: 49px; width: 360px; height: 372px;
    text-align: center; color: var(--ink);
  }
  .brand-mark {
    width: 58px; height: 58px; border-radius: 50%; background: var(--ink);
    margin: 48px auto 0;
  }
  .brand-name {
    font-family: 'Cinzel', serif; font-weight: 600; font-size: 30px;
    letter-spacing: 1px; margin-top: 18px; line-height: 1;
  }
  .vintage { font-family: 'Tinos', serif; font-size: 19px; margin-top: 40px; line-height: 1; }
  .varietal {
    font-family: 'Cinzel', serif; font-weight: 600; font-size: 19px;
    margin-top: 5px; line-height: 1; letter-spacing: .5px;
  }
  .appellation { font-family: 'Tinos', serif; font-size: 16px; margin-top: 5px; line-height: 1; }
  .region {
    font-family: 'Cinzel', serif; font-weight: 600; font-size: 11.5px;
    margin-top: 22px; letter-spacing: .3px;
  }

  .back-text {
    position: absolute; left: 100px; top: 442px; width: 160px;
    font-family: 'Tinos', serif; color: var(--accent); text-align: center;
    font-size: 9.6px; line-height: 1.38;
  }
  .sulfites { margin-top: 14px; }
  .specs { display: flex; justify-content: space-between; margin-top: 14px; padding: 0 4px; }
</style>
</head>
<body>
<main class="canvas">

  <section class="label label--gold">
    <div class="back-strip"><div class="back-strip__frame"></div></div>
    <div class="stars">
      <svg viewBox="0 0 24 24"><path d="M12 1l3.2 7.2 7.8.7-5.9 5.2 1.8 7.7L12 17.8 5.1 21.8l1.8-7.7L1 8.9l7.8-.7z"/></svg>
      <svg viewBox="0 0 24 24"><path d="M12 1l3.2 7.2 7.8.7-5.9 5.2 1.8 7.7L12 17.8 5.1 21.8l1.8-7.7L1 8.9l7.8-.7z"/></svg>
      <svg viewBox="0 0 24 24"><path d="M12 1l3.2 7.2 7.8.7-5.9 5.2 1.8 7.7L12 17.8 5.1 21.8l1.8-7.7L1 8.9l7.8-.7z"/></svg>
    </div>
    <div class="shield">
      <svg viewBox="0 0 360 372">
        <defs>
          <linearGradient id="goldFill" x1="0" y1="0" x2="1" y2="0.3">
            <stop offset="0" stop-color="var(--gold-dark)"/>
            <stop offset="0.3" stop-color="var(--gold-mid)"/>
            <stop offset="0.7" stop-color="var(--gold-light)"/>
            <stop offset="1" stop-color="var(--gold-dark)"/>
          </linearGradient>
        </defs>
        <path d="M28 4 H332 L338 22 L326 36 Q360 110 358 190 Q350 330 180 368 Q10 330 2 190 Q0 110 34 36 L22 22 Z" fill="url(#goldFill)"/>
        <path d="M40 14 H320 L325 25 L312 40 Q346 112 344 190 Q336 320 180 354 Q24 320 16 190 Q14 112 48 40 L35 25 Z" fill="none" stroke="var(--ink)" stroke-width="2.5"/>
      </svg>
    </div>
    <div class="front-text">
      <div class="brand-mark"></div>
      <div class="brand-name">Brindor Ranch</div>
      <div class="vintage">2022</div>
      <div class="varietal">Sauvignon Blanc</div>
      <div class="appellation">California</div>
      <div class="region">Palos Verdes Peninsula</div>
    </div>
    <div class="back-text">
      <p>GOVERNMENT WARNING: (1) According to the Surgeon General, women should not drink alcoholic beverages during pregnancy because of the risk of birth defects. (2) Consumption of alcoholic beverages impairs your ability to drive a car or operate machinery, and may cause health problems.</p>
      <p class="sulfites">Contains Sulfates.</p>
      <p class="specs"><span>750ML</span><span>Alc. 12.5% by Vol.</span></p>
    </div>
  </section>

  <section class="label label--silver">
    <div class="back-strip"><div class="back-strip__frame"></div></div>
    <div class="stars">
      <svg viewBox="0 0 24 24"><path d="M12 1l3.2 7.2 7.8.7-5.9 5.2 1.8 7.7L12 17.8 5.1 21.8l1.8-7.7L1 8.9l7.8-.7z"/></svg>
      <svg viewBox="0 0 24 24"><path d="M12 1l3.2 7.2 7.8.7-5.9 5.2 1.8 7.7L12 17.8 5.1 21.8l1.8-7.7L1 8.9l7.8-.7z"/></svg>
      <svg viewBox="0 0 24 24"><path d="M12 1l3.2 7.2 7.8.7-5.9 5.2 1.8 7.7L12 17.8 5.1 21.8l1.8-7.7L1 8.9l7.8-.7z"/></svg>
    </div>
    <div class="shield">
      <svg viewBox="0 0 360 372">
        <defs>
          <linearGradient id="silverFill" x1="0" y1="0" x2="1" y2="0.3">
            <stop offset="0" stop-color="var(--silver-dark)"/>
            <stop offset="0.35" stop-color="var(--silver-light)"/>
            <stop offset="0.7" stop-color="var(--silver-mid)"/>
            <stop offset="1" stop-color="var(--silver-dark)"/>
          </linearGradient>
        </defs>
        <path d="M28 4 H332 L338 22 L326 36 Q360 110 358 190 Q350 330 180 368 Q10 330 2 190 Q0 110 34 36 L22 22 Z" fill="url(#silverFill)"/>
        <path d="M40 14 H320 L325 25 L312 40 Q346 112 344 190 Q336 320 180 354 Q24 320 16 190 Q14 112 48 40 L35 25 Z" fill="none" stroke="var(--ink)" stroke-width="2.5"/>
      </svg>
    </div>
    <div class="front-text">
      <div class="brand-mark"></div>
      <div class="brand-name">Brindor Ranch</div>
      <div class="vintage">2022</div>
      <div class="varietal">Cabernet Sauvignon</div>
      <div class="appellation">California</div>
      <div class="region">Palos Verdes Peninsula</div>
    </div>
    <div class="back-text">
      <p>GOVERNMENT WARNING: (1) According to the Surgeon General, women should not drink alcoholic beverages during pregnancy because of the risk of birth defects. (2) Consumption of alcoholic beverages impairs your ability to drive a car or operate machinery, and may cause health problems.</p>
      <p class="sulfites">Contains Sulfates.</p>
      <p class="specs"><span>750ML</span><span>Alc. 13.5% by Vol.</span></p>
    </div>
  </section>

</main>
</body>
</html>
```